B2B Umbrella Site Requires Simple, Stylish Slider Designs

We're a dynamic promotional merchandise business in the process of building a new B2B Umbrella Store. It's our goal to provide printed umbrellas to suit the needs of our clients. Our main page is in need of ONE large key banner and THREE smaller sub category banners. We would like to see designs that use grey and green (or similar) to match with the theme of our layout. See: http://canopyvault.com.au/

The final designs should convey the desirability of our umbrellas while looking slick and modern in style. Please find attached our place holder banners for size reference and umbrella images to use in designs. If you require any further details or content, feel free to contact us.

Target Market(s)

Professionals and businesses across a wide range of fields. We offer a customisable product so we are as flexible as our target market.

Industry/Entity Type

Building

Font styles to use
Sans Serif

Requirements
Must have
• Must match sizes of attached sample graphics (
sub_banner + main_banner images). Must feature umbrella images attached to the brief - pick which images suit your design, but please ensure they are the correct umbrella style for the banner text. Clear, stylish text based on existing text found on sample graphics.
Nice to have
• Colours similar to the ones existing on the website already.
Should not have
• No serif fonts or clipart. Colours that do not facilitate easy reading.

```html
<!DOCTYPE html>
<html lang="en">
<head>
<meta charset="utf-8">
<title>CanopyVault – Promotional Umbrellas</title>
<link href="https://fonts.googleapis.com/css2?family=Roboto:wght@400;500;700&family=Lato:wght@400;700;900&display=swap" rel="stylesheet">
<style>
:root{
  --green:#7dc243;
  --green-dark:#6aa92f;
  --nav-top:#8dc800;
  --nav-bottom:#76b500;
  --ink:#333333;
  --ink-soft:#555555;
  --label:#666666;
  --rule:#cccccc;
  --panel:#f7f7f7;
  --panel-border:#d6d6d6;
  --banner-bg:#ececec;
  --banner-dark:#3d3d3d;
  --banner-band:#6f6f6f;
  --white:#ffffff;
}
*{box-sizing:border-box;margin:0;padding:0}
html,body{width:1200px;height:1000px;overflow:hidden;background:var(--white);font-family:"Roboto",Arial,sans-serif;color:var(--ink)}
.page{position:relative;width:1200px;height:1000px;overflow:hidden}
.rule{position:absolute;left:0;width:1200px;height:1px;background:var(--rule)}
.brand{position:absolute;left:14px;top:44px;display:flex;align-items:center;gap:8px}
.brand-name{font-family:"Roboto",sans-serif;font-weight:700;font-size:38px;color:var(--green);letter-spacing:-0.5px}
.brand-dot{width:16px;height:16px;border-radius:50%;background:#b9bccb}
.search{position:absolute;left:519px;top:51px;display:flex;gap:4px}
.search-field{width:200px;height:32px;border:1px solid #c8c8c8;border-radius:3px;background:var(--white)}
.search-button{width:79px;height:33px;border:none;border-radius:3px;background:var(--ink);color:var(--white);font:500 13px "Roboto",sans-serif}
.main-nav{position:absolute;left:14px;top:105px;width:1170px;height:46px;background:linear-gradient(var(--nav-top),var(--nav-bottom));border-radius:3px;box-shadow:0 2px 4px rgba(0,0,0,.25);display:flex}
.main-nav a{display:flex;align-items:center;padding:0 20px;color:var(--white);text-decoration:none;font-size:15px;border-right:1px solid rgba(255,255,255,.75)}
.panel-title{position:absolute;background:var(--panel);border:1px solid var(--panel-border);border-radius:3px;box-shadow:0 2px 3px rgba(0,0,0,.12);font-size:18px;color:var(--ink);padding-left:18px;display:flex;align-items:center}
.category-list{position:absolute;left:20px;top:292px;width:256px;list-style:none}
.category-list li{height:38px;display:flex;align-items:center;font-size:12px;font-weight:700;color:var(--ink);border-bottom:1px dotted #888}
.category-list li:last-child{border-bottom:none}
.enquiry{position:absolute;left:20px;top:640px;width:258px}
.enquiry label{display:block;font-size:12px;color:var(--label);height:31px;line-height:16px}
.enquiry .field{height:32px;border:1px solid #c8c8c8;border-radius:3px;margin-bottom:20px;background:var(--white)}
.enquiry .area{height:70px;border:1px solid #c8c8c8;border-radius:3px}
.hero{position:absolute;left:314px;top:213px;width:870px;height:359px;background:var(--banner-bg);overflow:hidden;font-family:"Lato",sans-serif}
.hero-band{position:absolute;left:0;bottom:0;width:100%;height:57px;background:var(--banner-band)}
.hero-headline{position:absolute;left:28px;top:0;width:420px;height:184px;background:#d8d8d8;padding:0 13px 13px}
.hero-headline div{width:100%;height:100%;background:var(--banner-dark);color:var(--white);text-align:center;font-weight:700;font-size:35px;line-height:41px;padding-top:14px;text-transform:uppercase}
.accent{color:var(--green)}
.hero-copy{position:absolute;left:38px;top:201px;width:400px;text-align:center;font-size:17px;line-height:21px;color:var(--ink-soft)}
.hero-button{position:absolute;left:142px;top:283px;width:193px;height:43px;background:linear-gradient(#86c341,#5f9a2a);color:#2b3a1a;font-weight:900;font-size:16px;display:flex;align-items:center;justify-content:center;box-shadow:0 2px 3px rgba(0,0,0,.3)}
.hero-photo{position:absolute;left:476px;top:0;width:394px;height:359px;background:linear-gradient(135deg,#eef3f6 0%,#7cc6ec 30%,#9ccf5a 60%,#d82a2a 62%,#c81c1c 100%)}
.tiles{position:absolute;left:314px;top:573px;width:870px;height:158px;display:flex;justify-content:space-between}
.tile{position:relative;width:288px;height:158px;border:3px solid #444;outline:1px solid #999;outline-offset:-6px;background:linear-gradient(#f4f4f4,#e2e2e2);font-family:"Lato",sans-serif;overflow:hidden}
.tile-text{position:absolute;z-index:1;left:8px;top:44px;color:var(--ink);font-size:17px;line-height:18px;text-transform:uppercase;white-space:nowrap}
.tile-text strong{display:block;color:var(--green);font-size:29px;line-height:30px;font-weight:700}
.tile-text small{font-size:14px;font-weight:700}
.tile-image{position:absolute;right:6px;top:12px;width:92px;height:132px;border-radius:46px 46px 10px 10px}
.products-title{left:314px;top:778px;width:870px;height:44px}
.product-card{position:absolute;top:850px;width:270px;height:160px;border:1px solid #d0d0d0;border-radius:3px;background:var(--white)}
.badge{position:absolute;left:10px;top:10px;padding:3px 7px;background:#f1f1f1;border:1px solid #e0e0e0;font-size:12px;color:var(--green-dark)}
.product-image{position:absolute;left:43px;top:43px;width:182px;height:120px;background:#f5f5f5}
.page-foot{position:absolute;left:0;top:956px;width:1200px;height:44px;background:var(--white)}
</style>
</head>
<body>
<div class="page">
  <div class="rule" style="top:4px"></div>

  <header>
    <div class="brand"><span class="brand-name">CanopyVault</span><span class="brand-dot"></span></div>
    <form class="search"><div class="search-field"></div><button class="search-button" type="button">Search</button></form>
    <nav class="main-nav">
      <a>Home</a><a>Fast Delivery</a><a>Testimonials</a><a>Sampling</a><a>Contact Us</a><a>FAQ</a>
    </nav>
  </header>

  <div class="rule" style="top:181px"></div>

  <aside>
    <div class="panel-title" style="left:14px;top:212px;width:270px;height:46px">Categories</div>
    <ul class="category-list">
      <li>Childrens Umbrellas</li><li>Folding Umbrellas</li><li>Medium Umbrellas</li>
      <li>Big Golf Umbrellas</li><li>Beach Umbrellas</li><li>Cafe Umbrellas</li>
    </ul>
    <div class="panel-title" style="left:14px;top:546px;width:270px;height:46px">Enquiry</div>
    <form class="enquiry">
      <label>Name:</label><div class="field"></div>
      <label>Phone:</label><div class="field"></div>
      <label>Email:</label><div class="field"></div>
      <label>Product Detail:</label><div class="area"></div>
    </form>
  </aside>

  <main>
    <section class="hero">
      <div class="hero-photo" role="img" aria-label="Woman in a red dress holding an open red branded umbrella against a sunny sky"></div>
      <div class="hero-band"></div>
      <div class="hero-headline"><div>Australias<br>Top <span class="accent">Promotional</span><br>Umbrella Vendor</div></div>
      <p class="hero-copy">Massive selection of <span class="accent">umbrellas</span><br>in stock and ready to be printed with your<br><span class="accent">logo</span> or slogan.</p>
      <div class="hero-button">VIEW ALL PRODUCTS</div>
    </section>

    <section class="tiles">
      <div class="tile">
        <div class="tile-text">Medium<strong>Corporate</strong><small>Umbrellas</small></div>
        <div class="tile-image" role="img" aria-label="Dark maroon corporate umbrella with curved handle" style="background:linear-gradient(#6a1f1a,#3e0f0c)"></div>
      </div>
      <div class="tile">
        <div class="tile-text" style="left:32px">Portable<strong>Folding</strong><small>Umbrellas</small></div>
        <div class="tile-image" role="img" aria-label="Red compact folding umbrella" style="background:linear-gradient(#e83a2f,#b91d16)"></div>
      </div>
      <div class="tile">
        <div class="tile-text" style="left:43px">Popular<strong>Golf</strong><small>Umbrellas</small></div>
        <div class="tile-image" role="img" aria-label="Green and white golf umbrella" style="background:linear-gradient(90deg,#f4f4f4,#1f5a1f)"></div>
      </div>
    </section>

    <div class="panel-title products-title">New Products</div>
    <div class="product-card" style="left:314px"><span class="badge">New</span><div class="product-image" role="img" aria-label="Product image placeholder"></div></div>
    <div class="product-card" style="left:613px"><span class="badge">New</span><div class="product-image" role="img" aria-label="Product image placeholder"></div></div>
    <div class="product-card" style="left:913px"><span class="badge">New</span><div class="product-image" role="img" aria-label="Product image placeholder"></div></div>
  </main>

  <div class="page-foot"></div>
</div>
</body>
</html>
```